Cover Design For eBook "Quill"

I need two e-book covers with the same look and feel:

first one:
title
THE QUILL MOVEMENT
subtitle
WIDEN ONLINE SUPPORT
author
MAPLEWAY GIFTS (just include the logo I attach)

second eBook
title
THE QUILL METHOD
subtitle
5 STEPS TO WIDEN YOUR CHURCH'S ONLINE SUPPORT
author
MAPLEWAY GIFTS (just include the log I attach)

Industry/Entity Type

Digital

Colors
f04a50
f68e4e
faa54b
ffcf3e

Requirements
Must have
• the MAPLEWAY GIFTS LOGO I attached at the bottom of the design.
• There needs to be some type of spark coming off of one of the letters in QUILL
Nice to have
• I'd love to have a horizontal and vertical layout

```html
<!DOCTYPE html>
<html lang="en">
<head>
<meta charset="utf-8">
<title>The Quill eBook Covers</title>
<link rel="stylesheet" href="https://fonts.googleapis.com/css2?family=Archivo+Black&family=Montserrat:wght@700&display=swap">
<style>
  :root {
    --coral: #f04a50;
    --peach: #f68e4e;
    --amber: #faa54b;
    --gold: #ffcf3e;
    --ink: #0b0b0c;
    --wine: #6e1414;
    --crimson: #c91f1f;
    --title-stroke: #2a0606;
    --subtitle: #f6c21a;
    --brand-text: #2b2b2b;
    --page: #ffffff;
  }
  * { margin: 0; padding: 0; box-sizing: border-box; }
  html, body {
    width: 1200px; height: 753px; overflow: hidden; background: var(--page);
  }
  .canvas { position: relative; width: 1200px; height: 753px; }
  .cover {
    position: absolute; top: 0; height: 753px; overflow: hidden;
  }
  .cover--movement { left: 0; width: 582px; }
  .cover--method { left: 620px; width: 580px; }

  .cover__art {
    position: absolute; left: 0; top: 0; width: 100%; height: 525px;
    background: linear-gradient(180deg, var(--ink) 0%, var(--ink) 14%, #3a0a0a 30%, var(--wine) 52%, #a51a1a 78%, var(--crimson) 100%);
  }
  .cover__sparks {
    position: absolute; left: -40px; top: 160px; width: calc(100% + 80px); height: 220px;
    background:
      radial-gradient(ellipse 55% 50% at 50% 50%, rgba(255, 207, 62, 0.6), rgba(250, 165, 75, 0.3) 60%, rgba(246, 142, 78, 0) 100%);
  }
  .cover__title {
    position: absolute; left: 0; width: 100%; text-align: center;
    font-family: "Archivo Black", sans-serif; line-height: 1;
    background: linear-gradient(180deg, #f56a6a 0%, var(--coral) 50%, #e0262c 100%);
    -webkit-background-clip: text; background-clip: text;
    color: transparent;
    -webkit-text-stroke: 2px var(--title-stroke);
  }
  .title--the { top: 128px; font-size: 76px; letter-spacing: 0; }
  .title--name { top: 222px; font-size: 112px; letter-spacing: 2px;
    background: linear-gradient(180deg, #ff8a3a 0%, var(--peach) 50%, var(--coral) 100%);
    -webkit-background-clip: text; background-clip: text; }
  .title--word { top: 365px; font-size: 70px; letter-spacing: 0; }

  .cover__quill {
    position: absolute; left: 0; top: 0; width: 100%; height: 525px;
  }

  .cover__band {
    position: absolute; left: 0; top: 525px; width: 100%; height: 73px;
    background: var(--ink);
    font-family: "Archivo Black", sans-serif; color: var(--subtitle);
  }
  .band__line--single {
    display: block; text-align: center; font-size: 29px; letter-spacing: 1.5px; line-height: 73px;
  }
  .band__lines {
    display: block; padding: 2px 0 0 48px; font-size: 28px; letter-spacing: 1.5px; line-height: 37px;
  }

  .cover__footer {
    position: absolute; left: 0; top: 598px; width: 100%; height: 155px;
    background: linear-gradient(180deg, var(--amber) 0%, #fbbb38 50%, var(--gold) 100%);
    display: flex; align-items: center; justify-content: center; gap: 14px;
    padding-bottom: 4px;
  }
  .brand__dot {
    width: 38px; height: 38px; border-radius: 50%; background: var(--coral);
  }
  .brand__name {
    font-family: "Montserrat", sans-serif; font-weight: 700; font-size: 27px;
    color: var(--brand-text); letter-spacing: 0.5px;
  }
</style>
</head>
<body>
<main class="canvas">

  <section class="cover cover--movement">
    <div class="cover__art"></div>
    <div class="cover__sparks" role="img" aria-label="Glowing golden sparks scattered behind the title"></div>
    <h1>
      <span class="cover__title title--the">THE</span>
      <span class="cover__title title--name">QUILL</span>
      <span class="cover__title title--word">MOVEMENT</span>
    </h1>
    <svg class="cover__quill" viewBox="0 0 582 525" aria-hidden="true">
      <defs>
        <linearGradient id="vane-a" x1="0" y1="1" x2="1" y2="0">
          <stop offset="0" stop-color="#f68e4e"/>
          <stop offset="1" stop-color="#ffcf3e"/>
        </linearGradient>
      </defs>
      <path d="M452 216 C 468 160 505 116 552 92 C 540 140 505 188 452 216 Z" fill="url(#vane-a)" stroke="#2a0606" stroke-width="2"/>
      <path d="M437 242 Q 492 160 552 92" fill="none" stroke="#2a0606" stroke-width="3" stroke-linecap="round"/>
    </svg>
    <p class="cover__band"><span class="band__line--single">WIDEN ONLINE SUPPORT</span></p>
    <footer class="cover__footer">
      <span class="brand__dot"></span>
      <span class="brand__name">MAPLEWAY GIFTS</span>
    </footer>
  </section>

  <section class="cover cover--method">
    <div class="cover__art"></div>
    <div class="cover__sparks" role="img" aria-label="Glowing golden sparks scattered behind the title"></div>
    <h1>
      <span class="cover__title title--the">THE</span>
      <span class="cover__title title--name">QUILL</span>
      <span class="cover__title title--word">METHOD</span>
    </h1>
    <svg class="cover__quill" viewBox="0 0 580 525" aria-hidden="true">
      <defs>
        <linearGradient id="vane-b" x1="0" y1="1" x2="1" y2="0">
          <stop offset="0" stop-color="#f68e4e"/>
          <stop offset="1" stop-color="#ffcf3e"/>
        </linearGradient>
      </defs>
      <path d="M451 216 C 467 160 504 116 551 92 C 539 140 504 188 451 216 Z" fill="url(#vane-b)" stroke="#2a0606" stroke-width="2"/>
      <path d="M436 242 Q 491 160 551 92" fill="none" stroke="#2a0606" stroke-width="3" stroke-linecap="round"/>
    </svg>
    <p class="cover__band"><span class="band__lines">5 STEPS TO WIDEN YOUR<br>CHURCH'S ONLINE SUPPORT</span></p>
    <footer class="cover__footer">
      <span class="brand__dot"></span>
      <span class="brand__name">MAPLEWAY GIFTS</span>
    </footer>
  </section>

</main>
</body>
</html>
```